Velnor Group: Business Card for a high end technology company

We need a cool new design for our business cards using our cloud logo. We are a technology consulting business. We pride ourselves on be the best of the best. We mainly focus on cloud solutions and managed services. We need a business card that sets us apart from the other technology companies in the area and allows us to stand out.

Target Market(s)

Technology departments, CIO, CEOs, and Information Technology Staff.

Industry/Entity Type

Information Technology

Contact Information for Business Card

Must have the logo and our name.
Must have employee name, email address, office phone, cell phone and website.
Need to have all info on one side a cool design on backside.

Font styles to use
Serif
Sans Serif

Requirements
Must have
• Must have the logo and our name.
• Must have employee name, email address, office phone, cell phone and website.
• Need to have all info on one side a cool design on back side.
• Must be a crisp clean design, not too busy or confusing.

```html
<!DOCTYPE html>
<html lang="en">
<head>
<meta charset="utf-8">
<title>Velnor Group — Business Card</title>
<link rel="stylesheet" href="https://fonts.googleapis.com/css2?family=Montserrat:wght@300;400;600&family=Open+Sans:wght@400;600&display=swap">
<style>
  :root {
    --backdrop: #3b322d;
    --card-dark: #1f1f21;
    --card-dark-edge: #2a2a2d;
    --blue-light: #5cc6ec;
    --blue-deep: #4a86cc;
    --accent: #4fb2ea;
    --text-light: #e9ecef;
    --text-muted: #c9cdd2;
    --divider: #3a3d42;
    --logo-grey: #55575c;
  }
  * { margin: 0; padding: 0; box-sizing: border-box; }
  html, body {
    width: 1200px; height: 844px; overflow: hidden;
    background: var(--backdrop);
  }
  .stage {
    position: relative; width: 1200px; height: 844px;
    display: flex; align-items: center; justify-content: center; gap: 60px;
  }
  .card {
    width: 525px; height: 300px; border-radius: 4px;
    position: relative; overflow: hidden;
    box-shadow: 0 12px 30px rgba(0,0,0,0.45);
  }
  /* Information side */
  .card--info {
    background: linear-gradient(135deg, var(--card-dark-edge), var(--card-dark));
    display: flex; align-items: center;
  }
  .brand-block {
    width: 285px; display: flex; flex-direction: column; align-items: center;
  }
  .brand {
    display: flex; align-items: center; gap: 10px;
    font-family: "Montserrat", sans-serif; font-weight: 300;
    font-size: 32px; color: var(--text-light); letter-spacing: 0.5px;
  }
  .brand__dot {
    width: 18px; height: 18px; border-radius: 50%; background: var(--accent);
  }
  .brand-url {
    margin-top: 8px; font-family: "Open Sans", sans-serif; font-weight: 600;
    font-size: 11px; color: var(--text-muted); letter-spacing: 0.5px;
  }
  .divider {
    width: 1px; height: 150px; background: var(--divider);
  }
  .contact {
    padding-left: 24px; font-family: "Open Sans", sans-serif;
  }
  .contact__name {
    font-weight: 600; font-size: 15px; color: var(--accent);
  }
  .contact__role {
    font-size: 12px; color: var(--text-light); margin-top: 1px;
  }
  .contact__list { list-style: none; margin-top: 22px; }
  .contact__item {
    display: flex; align-items: center; gap: 9px;
    font-size: 12.5px; color: var(--text-light); line-height: 19px;
  }
  .contact__icon { width: 10px; height: 10px; flex: none; }
  /* Design side */
  .card--back {
    background: linear-gradient(160deg, var(--blue-light), var(--blue-deep));
    display: flex; flex-direction: column; align-items: center; justify-content: center;
  }
  .card--back .brand { color: var(--logo-grey); font-size: 38px; }
  .card--back .brand-url { color: var(--logo-grey); font-size: 12px; }
</style>
</head>
<body>
<main class="stage">
  <section class="card card--info" aria-label="Business card, information side">
    <div class="brand-block">
      <div class="brand"><span class="brand__dot"></span>Velnor Group</div>
      <div class="brand-url">www.velnorgroup.com</div>
    </div>
    <div class="divider"></div>
    <div class="contact">
      <p class="contact__name">Marcus Hale</p>
      <p class="contact__role">Managing Director</p>
      <ul class="contact__list">
        <li class="contact__item">
          <svg class="contact__icon" viewBox="0 0 10 10"><path d="M2 0.5 L3.6 2.6 L2.8 3.6 Q4 6 6.4 7.2 L7.4 6.4 L9.5 8 L8.4 9.5 Q1 8.5 0.5 1.6 Z" fill="var(--accent)"/></svg>
          044-555 018 274
        </li>
        <li class="contact__item">
          <svg class="contact__icon" viewBox="0 0 10 10"><rect x="0.5" y="2" width="9" height="6.5" fill="var(--accent)"/><path d="M0.5 2 L5 5.6 L9.5 2" fill="none" stroke="var(--card-dark)" stroke-width="0.9"/></svg>
          hello@velnormail.com
        </li>
        <li class="contact__item">
          <svg class="contact__icon" viewBox="0 0 10 10"><circle cx="5" cy="5" r="4.5" fill="var(--accent)"/><path d="M0.5 5 H9.5 M5 0.5 Q2.5 5 5 9.5 M5 0.5 Q7.5 5 5 9.5" fill="none" stroke="var(--card-dark)" stroke-width="0.7"/></svg>
          www.velnorcloud.com
        </li>
      </ul>
    </div>
  </section>

  <section class="card card--back" aria-label="Business card, design side">
    <div class="brand">Velnor Group</div>
    <div class="brand-url">www.velnorgroup.com</div>
  </section>
</main>
</body>
</html>
```